Tech + Media Consulting Business // LOGO + Card

We need a logo design and business card for a Seattle-area strategy consulting firm. We believe in big, expansive thinking and we work for tech/media startups, as well as big companies like Quorvane and Tunelark. We would like designs inspired by the mountains and skies of Montana and Colorado. Existing logo attached but we would like a fresh approach.

Target Market(s)

Technology and Media Executives

Industry/Entity Type

Information Technology

Contact Information for Business Card

Marcus Lindholt
2157 61st Avenue NE
Medina WA 98027
Phone: 206-471-2958
marcuslindholt@ridgeframeadvisory.biz

Logo Text

Ridgeframe Advisory LLC

Font styles to use
Sans Serif

Colors

Designer to choose colors to be used in the design.

Requirements
Must have
• Logo inspired by mountains and sky.
• Our company wants to inspire our clients to think expansively -- embracing exploration and new ideas.
Nice to have
• Colors inspired by Fernwald-brand.
• We don't have a website at present but would like a field to add one later. Until then, we may reference our LinkedIn page:
• https://www.linkedin.com/company/ridgeframe-advisory-llc-nw

```html
<!DOCTYPE html>
<html lang="en">
<head>
<meta charset="utf-8">
<title>Ridgeframe Advisory LLC — Business Card</title>
<link href="https://fonts.googleapis.com/css2?family=Open+Sans:wght@400;600;700&display=swap" rel="stylesheet">
<style>
  :root {
    --page-bg: #f4f4f4;
    --card-light-top: #f2f2f2;
    --card-light-bottom: #c9c9c9;
    --card-dark: #111214;
    --card-dark-edge: #1d1f22;
    --brand-blue: #1457b8;
    --brand-orange: #f07a22;
    --ink: #1b1b1b;
    --text-light: #ffffff;
    --text-muted: #d8d8d8;
    --divider: #8a8a8a;
  }
  * { box-sizing: border-box; margin: 0; padding: 0; }
  html, body {
    width: 1200px; height: 900px; overflow: hidden;
    background: var(--page-bg);
    font-family: "Open Sans", Arial, sans-serif;
  }
  .business-card {
    position: absolute; left: 100px; top: 164px;
    width: 1000px; height: 572px;
    border-radius: 34px; overflow: hidden;
    box-shadow: 0 18px 40px rgba(0,0,0,0.22);
  }
  .card-top {
    position: absolute; left: 0; top: 0; width: 100%; height: 296px;
    background: linear-gradient(135deg, var(--card-light-top) 0%, #dcdcdc 45%, var(--card-light-bottom) 100%);
  }
  .brand-line {
    position: absolute; left: 0; top: 296px; width: 100%; height: 9px;
    background: var(--brand-blue);
  }
  .card-bottom {
    position: absolute; left: 0; top: 305px; width: 100%; height: 267px;
    background: linear-gradient(180deg, var(--card-dark-edge) 0%, var(--card-dark) 100%);
  }
  .wordmark {
    position: absolute; left: 0; top: 0; width: 100%; height: 296px;
    display: flex; align-items: center; justify-content: center; gap: 22px;
  }
  .wordmark-square {
    width: 46px; height: 46px; background: var(--brand-orange);
  }
  .wordmark-name {
    font-size: 50px; font-weight: 700; color: var(--ink);
    letter-spacing: 1px;
  }
  .holder {
    position: absolute; right: 560px; top: 90px; text-align: right;
  }
  .holder-name {
    font-size: 30px; font-weight: 700; color: var(--brand-orange);
  }
  .holder-title {
    margin-top: 10px; font-size: 17px; color: var(--text-muted);
    letter-spacing: 0.5px;
  }
  .divider {
    position: absolute; left: 486px; top: 30px; width: 1px; height: 200px;
    background: var(--divider);
  }
  .contact-list {
    position: absolute; left: 518px; top: 34px; list-style: none;
  }
  .contact-item {
    display: flex; align-items: flex-start; gap: 14px;
    font-size: 19px; color: var(--text-light); line-height: 28px;
    margin-bottom: 8px;
  }
  .contact-icon { flex: 0 0 28px; width: 28px; height: 28px; }
</style>
</head>
<body>
  <div class="business-card">
    <div class="card-top" role="img" aria-label="Light grey faceted background texture"></div>
    <div class="wordmark">
      <span class="wordmark-square"></span>
      <span class="wordmark-name">Ridgeframe Advisory LLC</span>
    </div>
    <div class="brand-line"></div>
    <div class="card-bottom" role="img" aria-label="Dark dotted background texture">
      <div class="holder">
        <div class="holder-name">Marcus Lindholt</div>
        <div class="holder-title">MANAGER</div>
      </div>
      <div class="divider"></div>
      <ul class="contact-list">
        <li class="contact-item">
          <svg class="contact-icon" viewBox="0 0 28 28"><circle cx="14" cy="14" r="14" fill="#f07a22"/><path d="M9.5 7.5l3 3-1.6 1.8c.8 1.8 2.2 3.2 4 4l1.8-1.6 3 3-2 2c-5 0-10.2-5.2-10.2-10.2z" fill="#111214"/></svg>
          <span>206-471-2958</span>
        </li>
        <li class="contact-item">
          <svg class="contact-icon" viewBox="0 0 28 28"><circle cx="14" cy="14" r="14" fill="#f07a22"/><rect x="7.5" y="9.5" width="13" height="9" fill="none" stroke="#111214" stroke-width="1.6"/><path d="M7.5 9.5l6.5 5 6.5-5" fill="none" stroke="#111214" stroke-width="1.6"/></svg>
          <span>marcuslindholt@ridgeframeadvisory.biz</span>
        </li>
        <li class="contact-item">
          <svg class="contact-icon" viewBox="0 0 28 28"><circle cx="14" cy="14" r="14" fill="#f07a22"/><circle cx="14" cy="14" r="7" fill="none" stroke="#111214" stroke-width="1.5"/><ellipse cx="14" cy="14" rx="3" ry="7" fill="none" stroke="#111214" stroke-width="1.3"/><path d="M7 14h14" stroke="#111214" stroke-width="1.3"/></svg>
          <span>www.ridgeframeadvisory.com</span>
        </li>
        <li class="contact-item">
          <svg class="contact-icon" viewBox="0 0 28 28"><circle cx="14" cy="14" r="14" fill="#f07a22"/><path d="M14 6.5a5 5 0 0 1 5 5c0 3.8-5 9.5-5 9.5s-5-5.7-5-9.5a5 5 0 0 1 5-5z" fill="#111214"/><circle cx="14" cy="11.5" r="2" fill="#f07a22"/></svg>
          <span>2157 61st Avenue NE<br>Medina WA 98027</span>
        </li>
      </ul>
    </div>
  </div>
</body>
</html>
```